Tidal Arena Play - "Corvana of Sports" design needed

We need a web design created for Tidal Arena Play. This includes these separate page
The Site map needed has been updated and available to you in Adobe Muse.....
1) Landing Page / Home page
2) Authentication login / Sign up page
3) After logged in - All Content Page
- IE: Corvana
4) Once a thumbnail is selected - Content player and other similar content thumbnails
- IE: Corvana
4) Generic pages for content fields - terms / policies / contact us / information / etc
5) Generic pages for customer input content fields - My profile / payment / account information / cancellation page
Important for Project Selection.....
A - Design needs to be for Desktop and Mobile.
B - The best example I can point to - that so long as skinned similarly to our
branding at TidalArenaPlay is corvana.example or KVRT MORE or Zepo
C - Final design needs to be in layered in PSD and AI
D - Attached is our old design that needs an updated concept. Format has been
done in Adobe Muse.

```html
<!DOCTYPE html>
<html lang="en">
<head>
<meta charset="utf-8">
<title>Tidal Arena Play</title>
<link href="https://fonts.googleapis.com/css2?family=Lato:ital,wght@0,300;0,400;0,700;0,900;1,400&family=Roboto+Condensed:wght@400;700&family=Signika:wght@300;400;600&display=swap" rel="stylesheet">
<style>
:root{
  --red:#e21b1b;
  --red-dark:#b01414;
  --yellow:#ffd200;
  --black:#000;
  --ink:#1a1a1a;
  --white:#fff;
  --grey:#8a8a8a;
  --light:#f1f1f1;
}
*{margin:0;padding:0;box-sizing:border-box}
html,body{width:699px;height:1200px;overflow:hidden;background:var(--white)}
body{position:relative;font-family:"Lato",sans-serif;color:var(--white)}
.abs{position:absolute}
.cond{font-family:"Roboto Condensed",sans-serif}

/* hero */
.hero{left:0;top:0;width:699px;height:356px;background:linear-gradient(120deg,#2b1418 0%,#4a2026 35%,#202636 70%,#131722 100%)}
.brand-name{font-size:15px;font-weight:700;letter-spacing:.5px;color:var(--white);white-space:nowrap}
.brand-top{left:96px;top:38px}
.account{left:584px;top:30px;font-size:10px;font-weight:900;letter-spacing:-.2px}
.burger{left:654px;top:31px;width:14px;height:9px;border-top:2px solid var(--red);border-bottom:2px solid var(--red)}
.burger::after{content:"";position:absolute;left:0;top:1.5px;width:14px;height:2px;background:var(--red)}
.feat-label{left:98px;top:171px;font-size:8px}
.arrow-box{left:94px;width:18px;height:18px;display:flex;align-items:center;justify-content:center}
.arrow-up{top:192px;border:1px solid #ccc}
.arrow-down{top:214px;background:var(--red)}
.hero-title{left:122px;top:187px;font-family:"Signika",sans-serif;font-size:19px;font-weight:400}
.hero-desc{left:122px;top:213px;width:232px;font-size:6px;line-height:8.5px}
.stream-btn{left:123px;top:250px;width:66px;height:19px;background:var(--yellow);color:var(--ink);font-size:6.5px;display:flex;align-items:center;justify-content:center}
.dots{left:124px;top:285px;display:flex;gap:2px}
.dots span{width:3px;height:3px;border-radius:50%;background:var(--white)}
.dots span:first-child{background:none;border:1px solid var(--white)}
.price-box{left:486px;top:166px;width:162px;height:127px;background:rgba(190,22,22,.92);text-align:center;padding-top:22px}
.price-box::after{content:"";position:absolute;right:0;top:0;border-top:8px solid var(--yellow);border-left:8px solid transparent}
.price-line{font-family:"Roboto Condensed",sans-serif;font-size:11px}
.price-line b{font-size:15px;font-weight:400}
.price-rule{width:16px;height:3px;border-top:1px solid #fff;border-bottom:1px solid #fff;margin:7px auto 9px}
.price-text{font-family:"Lato",sans-serif;font-size:10.5px;font-style:italic;line-height:13.5px;padding:0 14px}

/* nav */
.nav{left:0;top:356px;width:699px;height:27px;background:var(--red);border-bottom:2px solid var(--red-dark)}
.nav ul{position:absolute;left:153px;top:0;height:27px;list-style:none;display:flex;align-items:center;font-size:5.6px;font-family:"Roboto Condensed",sans-serif}
.nav li{padding:0 6px;height:27px;line-height:27px}
.nav li.active{background:var(--red-dark);padding:0 8px}
.nav li.member{color:var(--yellow);padding-left:14px}

/* intro */
.intro{left:0;top:383px;width:699px;height:400px;background:var(--black)}
.mark-icon{left:327px;top:402px}
.welcome-sub{left:0;width:699px;top:425px;text-align:center;color:var(--yellow);font-size:9.5px}
.welcome-title{left:0;width:699px;top:437px;text-align:center;font-size:18px;font-weight:700}
.mission-head{left:94px;top:475px;border-left:3px solid var(--yellow);padding-left:10px;font-size:12.5px;font-weight:700;color:var(--grey);line-height:12px;width:84px}
.mission-head::after{content:"";position:absolute;right:0;top:0;border-top:6px solid var(--red);border-left:6px solid transparent}
.quote-mark{left:94px;top:536px;color:var(--red);font-size:26px;font-family:Georgia,serif;font-weight:700;line-height:20px}
.mission-text{left:117px;top:536px;width:215px;font-family:Georgia,serif;font-style:italic;font-size:8px;line-height:11px;color:var(--white)}
.mission-text p+p{margin-top:10px}
.mission-rule{left:118px;top:639px;width:18px;height:2px;background:#666}
.faded-name{left:118px;top:674px;font-size:11px;font-weight:700;color:#777;white-space:nowrap}
.thumb{top:478px;width:75px;height:123px}
.play{left:24px;top:49px;width:26px;height:26px;border-radius:50%;border:2px solid #fff;background:rgba(0,0,0,.35)}
.play::after{content:"";position:absolute;left:9px;top:6px;border-left:8px solid #fff;border-top:5px solid transparent;border-bottom:5px solid transparent}
.pkg-title{left:356px;top:616px;font-size:12px;font-family:"Signika",sans-serif;font-weight:300}
.pkg-title b{font-weight:400}
.pkg-text{left:357px;top:639px;width:250px;font-size:5.6px;line-height:8.5px;color:#ddd}

/* about */
.about-icon{left:327px;top:773px}
.about-title{left:0;width:699px;top:794px;text-align:center;color:var(--ink);font-size:18px;font-weight:900;letter-spacing:-.3px}
.tagline{left:273px;top:816px;width:153px;height:12px;background:var(--red);font-size:7.5px;letter-spacing:1.4px;display:flex;align-items:center;justify-content:center;font-family:"Roboto Condensed",sans-serif}
.sport{top:855px;width:108px;text-align:center;color:var(--ink)}
.sport-box{position:relative;width:44px;height:44px;margin:0 auto;background:var(--light);display:flex;align-items:center;justify-content:center}
.sport-box::after{content:"";position:absolute;right:0;top:0;border-top:6px solid var(--red);border-left:6px solid transparent}
.sport-box.dark{background:var(--ink);border:1.5px solid #555}
.sport h3{margin-top:14px;font-size:6.8px;font-weight:400;letter-spacing:.3px}
.sport.current h3{color:var(--red)}
.sport p{margin-top:5px;font-size:5.2px;line-height:8px;color:#444}

/* footer */
.footer{left:0;top:998px;width:699px;height:202px;background:linear-gradient(110deg,#1f1f22 0%,#2c2628 50%,#1d1f24 100%)}
.f-head{font-size:7.5px;font-family:"Roboto Condensed",sans-serif}
.f-about{left:79px;top:1027px}
.f-about::before{content:"";position:absolute;left:-2px;top:-3px;width:3px;height:3px;background:var(--red)}
.f-text{left:79px;top:1052px;width:135px;font-size:5px;line-height:11px;color:#ddd}
.f-news{left:77px;top:1111px}
.email{left:77px;top:1137px;width:83px;height:20px;background:#151515;font-size:5.5px;padding:7px 8px}
.submit{left:160px;top:1137px;width:35px;height:20px;background:var(--yellow);color:var(--ink);font-size:5.5px;font-weight:700;display:flex;align-items:center;justify-content:center}
.brand-foot{left:0;width:699px;top:1059px;text-align:center}
.rights{left:0;width:699px;top:1110px;text-align:center;font-size:4.8px;color:#ddd}
.social{left:290px;top:1137px;display:flex;gap:8px}
.social span{width:13px;height:13px;border-radius:50%;background:#777}
.f-videos{left:477px;top:1038px;color:var(--red);font-size:7px}
.vid{width:39px;height:39px;background:#a9a9a9;border:1.5px solid #8a8a8a;color:#cfcfcf;font-size:4.5px;display:flex;align-items:center;justify-content:center}
</style>
</head>
<body>

<section class="hero abs" role="img" aria-label="Paintball players in action during a match, darkened with a red tint"></section>

<div class="brand-name brand-top abs">TIDAL ARENA PLAY</div>
<div class="account abs">MY ACCOUNT</div>
<div class="burger abs"></div>

<div class="feat-label abs cond">FEATURED SPORTS</div>
<div class="arrow-box arrow-up abs"><svg width="8" height="5" viewBox="0 0 8 5"><path d="M1 4 4 1 7 4" fill="none" stroke="#fff" stroke-width="1.2"/></svg></div>
<div class="arrow-box arrow-down abs"><svg width="8" height="5" viewBox="0 0 8 5"><path d="M1 1 4 4 7 1" fill="none" stroke="#fff" stroke-width="1.2"/></svg></div>
<h1 class="hero-title abs">2015 PXA World Cup Final</h1>
<p class="hero-desc abs">Lorem Ipsum is simply dummy text of the printing and typesetting industry. Lorem Ipsum has been the industry's standard dummy text ever since the 1500s, when an unknown printer took a galley of type and scrambled it to make a type</p>
<div class="stream-btn abs">STREAM NOW</div>
<div class="dots abs"><span></span><span></span><span></span><span></span><span></span></div>

<aside class="price-box abs">
  <div class="price-line">Plans Starting @ <b>$5.99</b> / Month</div>
  <div class="price-rule"></div>
  <div class="price-text">Documentaries, alternative sports, and more! Live and on-demand. Anytime. Anywhere.</div>
</aside>

<nav class="nav abs">
  <ul>
    <li class="active">HOME</li><li>ABOUT</li><li>SPORTS</li><li>PAYMENT</li><li>PROFILE</li><li>VIDEOS</li><li>PRICE PLANS</li><li>ACCOUNT</li><li>CONTACT</li><li>FAQ</li><li class="member">BECOME A MEMBER</li>
  </ul>
</nav>

<section class="intro abs"></section>
<svg class="abs" style="left:0;top:728px" width="699" height="56" viewBox="0 0 699 56"><polygon points="0,50 442,1 699,34 699,56 0,56" fill="#fff"/></svg>

<svg class="mark-icon abs" width="45" height="14" viewBox="0 0 45 14"><line x1="0" y1="7" x2="13" y2="7" stroke="#777" stroke-width="1.5"/><line x1="32" y1="7" x2="45" y2="7" stroke="#777" stroke-width="1.5"/><circle cx="22.5" cy="7" r="5.5" fill="none" stroke="#e21b1b" stroke-width="2"/><path d="M21 4.5 25 7 21 9.5z" fill="#fff"/></svg>
<div class="welcome-sub abs">WELCOME TO</div>
<h2 class="welcome-title abs">TIDAL ARENA PLAY</h2>

<div class="mission-head abs">OUR MISSION STATEMENT</div>
<div class="quote-mark abs">&ldquo;</div>
<div class="mission-text abs">
  <p>We look forward to providing you with great live sporting events, documentaries, educational content, and original series.</p>
  <p>If you ever wish to cancel your membership with Tidal Arena Play, or opt-in or out of our email newsletters, you will find these options under the "My Account" link at the top of the screen.</p>
</div>
<div class="mission-rule abs"></div>
<div class="faded-name abs">TIDAL ARENA PLAY</div>

<div class="thumb abs" style="left:356px;background:linear-gradient(160deg,#6a7a3a,#c9a12a 50%,#2c6e8a)" role="img" aria-label="Series poster with a paintball player aiming"><div class="play abs"></div></div>
<div class="thumb abs" style="left:444px;background:linear-gradient(160deg,#c91e3a,#1e2a5a 60%,#111)" role="img" aria-label="Paintball player in a masked helmet"><div class="play abs" style="background:rgba(220,170,0,.8)"></div></div>
<div class="thumb abs" style="left:532px;background:linear-gradient(160deg,#555,#8a4a2a 50%,#2a2a2a)" role="img" aria-label="Paintball player in goggles close up"><div class="play abs"></div></div>
<h3 class="pkg-title abs">Tidal Arena Play <b>Premium Package</b></h3>
<p class="pkg-text abs">We look forward to providing you with great live sporting events, documentaries, educational content, and original series.<br>If you ever wish to cancel your membership with Tidal Arena Play, or opt-in or out of our email newsletters, you will find these options under the "My Account" link at the top of the screen.</p>

<svg class="about-icon abs" width="45" height="14" viewBox="0 0 45 14"><line x1="0" y1="7" x2="13" y2="7" stroke="#555" stroke-width="1.5"/><line x1="32" y1="7" x2="45" y2="7" stroke="#555" stroke-width="1.5"/><circle cx="22.5" cy="7" r="5" fill="none" stroke="#e21b1b" stroke-width="2"/><path d="M21 4.5 25 7 21 9.5z" fill="#e21b1b"/></svg>
<h2 class="about-title abs">ABOUT TIDAL ARENA</h2>
<div class="tagline abs">WE'RE ALL ABOUT XTREME SPORTS</div>

<div class="sport abs" style="left:98px">
  <div class="sport-box"><svg width="20" height="18" viewBox="0 0 20 18"><path d="M10 1 15 11 9 11z" fill="#111"/><circle cx="6" cy="9" r="1.6" fill="#111"/><path d="M2 13h14" stroke="#111" stroke-width="1.5"/><path d="M1 16q2-2 4 0t4 0 4 0 4 0" fill="none" stroke="#111" stroke-width="1.2"/></svg></div>
  <h3>FEATURED SPORT</h3>
  <p>Ut eu diam vel leo aliquam consectetu Proin torto elit rutrum donec rhoncu. Cras erad est cursus sed dignissim sed euismod</p>
</div>
<div class="sport current abs" style="left:230px">
  <div class="sport-box dark"><svg width="22" height="18" viewBox="0 0 22 18"><circle cx="5" cy="12" r="4" fill="none" stroke="#fff" stroke-width="1.5"/><circle cx="17" cy="12" r="4" fill="none" stroke="#fff" stroke-width="1.5"/><circle cx="13" cy="2.5" r="2" fill="#fff"/><path d="M5 12 9 6 13 9h4" fill="none" stroke="#fff" stroke-width="1.5"/></svg></div>
  <h3>FEATURED SPORT</h3>
  <p>Ut eu diam vel leo aliquam consectetu Proin torto elit rutrum donec rhoncu. Cras erad est cursus sed dignissim sed euismod</p>
</div>
<div class="sport abs" style="left:361px">
  <div class="sport-box"><svg width="16" height="20" viewBox="0 0 16 20"><path d="M3 1 8 8 13 1" fill="none" stroke="#111" stroke-width="1.5"/><circle cx="8" cy="13" r="5.5" fill="none" stroke="#111" stroke-width="1.5"/><path d="M7 11h1.5v5" fill="none" stroke="#111" stroke-width="1.3"/></svg></div>
  <h3>FEATURED SPORT</h3>
  <p>Ut eu diam vel leo aliquam consectetu Proin torto elit rutrum donec rhoncu. Cras erad est cursus sed dignissim sed euismod</p>
</div>
<div class="sport abs" style="left:492px">
  <div class="sport-box"><svg width="22" height="18" viewBox="0 0 22 18"><circle cx="11" cy="4" r="2.5" fill="#111"/><path d="M7 13q4-7 8 0z" fill="#111"/><path d="M2 14 20 8" stroke="#111" stroke-width="1.3"/><ellipse cx="11" cy="14" rx="9" ry="2" fill="#111"/></svg></div>
  <h3>FEATURED SPORT</h3>
  <p>Ut eu diam vel leo aliquam consectetu Proin torto elit rutrum donec rhoncu. Cras erad est cursus sed dignissim sed euismod</p>
</div>

<footer class="footer abs" role="img" aria-label="Dark faded photo of paintball players behind the footer"></footer>
<div class="f-head f-about abs">ABOUT TIDAL ARENA</div>
<p class="f-text abs">If you ever wish to cancel your membership with Tidal Arena Play, or opt-in or out of our email newsletters, you will find these options under the "My Account" link at the top of the screen.</p>
<div class="f-head f-news abs">NEWSLETTER SIGNUP</div>
<div class="email abs">Email ID ...</div>
<div class="submit abs">SUBMIT</div>

<div class="brand-name brand-foot abs">TIDAL ARENA PLAY</div>
<div class="rights abs">ALL RIGHTS RESERVED (C) 2018</div>
<div class="social abs"><span></span><span></span><span></span><span></span><span></span><span></span></div>

<div class="f-head f-videos abs">FEATURED VIDEOS</div>
<div class="vid abs" style="left:474px;top:1064px">90 x 90</div>
<div class="vid abs" style="left:520px;top:1064px">90 x 90</div>
<div class="vid abs" style="left:566px;top:1064px">90 x 90</div>
<div class="vid abs" style="left:474px;top:1109px">90 x 90</div>
<div class="vid abs" style="left:520px;top:1109px">90 x 90</div>
<div class="vid abs" style="left:566px;top:1109px">90 x 90</div>

</body>
</html>
```